Centro Renal Tova Quirandel

Redo a rough draft of the presentation. Some slides are just hand sketches. 15 slides total

Font styles to use
Sans Serif

Colors

Designer to choose colors to be used in the design.

Requirements
Must have
• Use the 'machine' on the dialysis slide. The kidney wherever you feel works to accentuate.
• The slide following the 'supporting cast' should be the same but 'centro vitrales norteños' in bold and maybe the picture vascular acces if works.
• Use the 4 puerto Halcón pictures for 'centro de dialisis puerto halcón' create 4 slides using one picture per slide; go big.
• Create a location slide before the last q&a slide using the location picture
Nice to have
• Please use elegant font for title
• Create something for the estadisticas 2016 slides; not a list like it is now

```html
<!DOCTYPE html>
<html lang="es">
<head>
<meta charset="utf-8">
<title>Centro Renal Tova Quirandel — Presentación</title>
<link href="https://fonts.googleapis.com/css2?family=Lato:wght@300;400;700&display=swap" rel="stylesheet">
<style>
  :root{
    --wine:#8e2a45;
    --wine-dark:#5e0f22;
    --ink:#1e1e1e;
    --paper:#ffffff;
    --bg-core:#f9a21c;
    --bg-edge:#b5520f;
  }
  *{margin:0;padding:0;box-sizing:border-box}
  html,body{width:1200px;height:900px;overflow:hidden}
  body{
    background:radial-gradient(ellipse 70% 60% at 50% 48%, var(--bg-core) 0%, #f27a1a 55%, var(--bg-edge) 100%);
    font-family:'Lato',sans-serif;color:var(--ink);position:relative;
  }
  .slide{position:absolute;width:334px;height:250px;background:var(--paper);overflow:hidden;box-shadow:0 1px 3px rgba(0,0,0,.18)}
  .col-1{left:98px}.col-2{left:447px}.col-3{left:795px}
  .row-1{top:165px}.row-2{top:429px}
  .band{position:absolute;left:0;right:0;top:229px;height:14px;background:var(--wine)}
  .band-end{position:absolute;right:0;top:229px;width:12px;height:14px;background:var(--wine-dark)}
  .brand{display:inline-flex;align-items:center;gap:3px;font-family:'Lato',sans-serif;font-weight:400;color:var(--ink);font-size:17px;letter-spacing:.2px}
  .brand-dot{width:14px;height:14px;border-radius:50%;background:var(--wine);display:inline-block}
  .photo{position:absolute}
  .cover-photo{left:0;top:0;width:334px;height:125px;background:linear-gradient(120deg,#d8d8e2 0%,#b9bccb 40%,#eae7ea 60%,#b02a34 85%,#e9dede 100%)}
  .cover-title{position:absolute;left:0;right:0;top:142px;text-align:center;font-weight:300;font-size:22px;color:var(--wine)}
  .cover-marks{position:absolute;left:0;right:0;top:190px;display:flex;justify-content:center;align-items:center;gap:28px}
  .badge{width:22px;height:22px;border-radius:50%;border:2px solid #c9a35a;background:#fbeedd}
  .portrait{left:205px;top:0;width:117px;height:250px}
  .portrait-a{background:linear-gradient(180deg,#e7e3df 0%,#c9b59a 30%,#1c1c1c 55%,#111 100%)}
  .portrait-b{background:linear-gradient(180deg,#eef1f3 0%,#b48a6c 30%,#1f2a36 55%,#141b24 100%)}
  .bio{position:absolute;right:142px;top:58px;width:190px;text-align:right;font-size:7px;line-height:9.5px}
  .bio .brand{margin-bottom:12px}
  .bio-name{font-size:9.5px;color:var(--wine);line-height:12px}
  .bio-label{font-size:7.5px;color:var(--wine);margin-top:9px}
  .section-head{position:absolute;left:28px;top:74px}
  .section-title{font-weight:300;font-size:22px;line-height:23px;color:var(--wine);margin-top:6px}
  .machine{left:205px;top:0;width:117px;height:250px;background:linear-gradient(160deg,#bfc4cb 0%,#e8e2dc 35%,#9a3040 60%,#c9c6c2 100%)}
  .fade{position:absolute;left:53px;top:0;width:152px;height:229px;background:linear-gradient(90deg,rgba(255,255,255,1),rgba(238,238,240,.9))}
  .dial-title{position:absolute;left:18px;top:62px;font-weight:300;font-size:22px;color:var(--wine)}
  .dial-list{position:absolute;left:18px;top:96px;width:170px;list-style:none;font-size:7px;line-height:9.5px}
  .dial-list .term{font-size:9.5px;color:var(--wine);line-height:12px}
  .dial-list .term::before{content:"• "}
  .stats-title{position:absolute;left:0;right:0;top:60px;text-align:center;font-weight:300;font-size:24px;color:var(--wine);letter-spacing:.5px}
  .stats-col{position:absolute;top:116px;list-style:none;font-size:10px;line-height:12px}
  .stats-col li::before{content:"• "}
  .stats-left{left:44px}.stats-right{left:187px}
</style>
</head>
<body>

<section class="slide col-1 row-1">
  <div class="photo cover-photo" role="img" aria-label="Primer plano de una máquina de diálisis con tubos rojos"></div>
  <h1 class="cover-title">Centro Renal Tova Quirandel</h1>
  <div class="cover-marks">
    <span class="badge"></span>
    <span class="brand"><span class="brand-dot"></span>nefralis</span>
  </div>
  <div class="band"></div>
</section>

<section class="slide col-2 row-1">
  <div class="bio">
    <span class="brand"><span class="brand-dot"></span>nefralis</span>
    <p class="bio-name">Marisol Quenter, MD</p>
    <p>Board Certified in Nephrology</p>
    <p>Medical Director Vitalis Ribera</p>
    <p class="bio-label">Former</p>
    <p>Nephrology Department Director Amparo Central</p>
    <p>Faculty Member, UIN School of Medicine</p>
  </div>
  <div class="band"></div>
  <div class="photo portrait portrait-a" role="img" aria-label="Retrato de la directora médica con chaqueta negra"></div>
</section>

<section class="slide col-3 row-1">
  <div class="bio">
    <span class="brand"><span class="brand-dot"></span>nefralis</span>
    <p class="bio-name">Ing. Tomás R. Velarde</p>
    <p>B.A. Civil Engineering</p>
    <p>Miembro Junta Directores Fundación Isleña del Riñón</p>
    <p class="bio-label">Desarrollador,</p>
    <p>Centro de Diálisis Puerto Halcón</p>
    <p>Solano Dialysis Centre</p>
  </div>
  <div class="band"></div>
  <div class="photo portrait portrait-b" role="img" aria-label="Retrato del ingeniero con traje oscuro"></div>
</section>

<section class="slide col-1 row-2">
  <div class="section-head">
    <span class="brand"><span class="brand-dot"></span>nefralis</span>
    <h2 class="section-title">Centro de Diálisis<br>Puerto Halcón</h2>
  </div>
  <div class="band"></div>
</section>

<section class="slide col-2 row-2">
  <div class="fade"></div>
  <h2 class="dial-title">Dialisis</h2>
  <ul class="dial-list">
    <li class="term">Agudo</li>
    <li>Tratamiento a pacientes con perdida repentina de función renal y usualmente temporera. Administrada en hospitales.</li>
    <li class="term">Crónico</li>
    <li>Tratamiento a pacientes con perdida permanente de función renal.</li>
  </ul>
  <div class="band"></div>
  <div class="photo machine" role="img" aria-label="Paciente conectado a una máquina de diálisis"></div>
</section>

<section class="slide col-3 row-2">
  <h2 class="stats-title">ESTADISTICAS 2016</h2>
  <ul class="stats-col stats-left">
    <li>PREVALENCIA 5841</li>
    <li>Mortalidad 1140</li>
    <li>Transplantes 95</li>
  </ul>
  <ul class="stats-col stats-right">
    <li>INCIDENCIA 1428</li>
    <li>Diabetes 66%</li>
    <li>Hipertensión 20%</li>
  </ul>
  <div class="band"></div>
  <div class="band-end"></div>
</section>

</body>
</html>
```